International online gaming platform needs a game UI design

1. We need a game interface for three kinds of theme based on our guideline and sample mockup.
2. The product type is the online casino games related, we need a series of casino games UIs, however, we can start on the game lobby first.
3. Three theme you might choose from or refer to:
A. 3D look & feel
B. Realistic casino theme
C. Richness and grandeur
D. European casino style
4. NOT ALLOWED to change the design layout.
MUST follow our sample mock up and ONLY redefine the design style.
5. All items must be in a stand-alone component, eg. Button, Tab, Icon,... etc.
6. We need the layout in vector shape, but we can review in JPG or PNG format.
7. The image size: 1366 x 768

Updated:
1. All items and their positions should be same as the sample UI we provided.
Please redesign all the items and create a new theme for it.
No need to create a new layout.
2. Although we accept the draft design, but all the items in UI should be completed.
3. All the wordings in the sample UI are confirmed, you might change the fonts.
4. For the avatar in the left hand side, you don't have to redraw it.
We already have our own avatar system implemented.
5. All the items such as icons, tabs, and buttons are free to redesign.

Dear designers,

We've increased our budget and raise the prize money to 800 USD.  
We also accept the draft design in PNG format and we can go through the details in handover stage.
Thank you very much. 

Reason: Dear designers, We decided to extend the deadline by 7 days. As mentioned in the task description, we are looking for a new style of design and you might refer to the below style. A. 3D look & feel B. Realistic casino theme C. Richness and grandeur D. European casino style If you are still interested in our project, please send us your work. Thank you very much!

Casino

```html
<!DOCTYPE html>
<html lang="en">
<head>
<meta charset="utf-8">
<title>Live Casino Lobby</title>
<link rel="stylesheet" href="https://fonts.googleapis.com/css2?family=Lora:wght@400;600;700&family=Pinyon+Script&family=Roboto:wght@400;500;700&display=swap">
<style>
:root{
  --gold-hi:#fde08a;
  --gold:#f0b23a;
  --gold-mid:#d8921f;
  --gold-dk:#8a5a12;
  --black:#0b0b0b;
  --panel:#1a1a1a;
  --felt:#1f7a32;
  --felt-dk:#0f4f1d;
  --wine:#7a1a1a;
  --wine-hi:#c0483a;
  --navy:#233a8c;
  --ink:#1b1308;
  --white:#ffffff;
  --grid:#d6d6d6;
}
*{box-sizing:border-box;margin:0;padding:0}
html,body{width:1200px;height:675px;overflow:hidden;background:var(--black)}
body{position:relative;font-family:"Roboto",sans-serif;color:var(--white)}
.abs{position:absolute}

/* top bar */
.topbar{left:0;top:0;width:1200px;height:40px;background:linear-gradient(#2a2a2a,#0a0a0a)}
.title-plate{left:0;top:0;width:440px;height:40px;background:linear-gradient(#ffd773,var(--gold-mid));clip-path:polygon(0 0,100% 0,93% 100%,0 100%)}
.title{left:60px;top:-6px;font-family:"Pinyon Script",cursive;font-size:40px;color:var(--ink)}
.sys-icons{left:1000px;top:0;width:200px;height:40px;background:linear-gradient(#3a3a3a,#111);clip-path:polygon(8% 0,100% 0,100% 100%,0 100%);display:flex;gap:10px;align-items:center;padding-left:28px}
.sys-icons svg{width:24px;height:24px}

/* sidebar */
.sidebar{left:0;top:40px;width:188px;height:595px;background:linear-gradient(90deg,#e79a2a,#f5bd4c 50%,#e39526)}
.avatar-frame{left:16px;top:54px;width:156px;height:240px;background:#1c1c1c;border-radius:6px;border:2px solid #111}
.avatar{left:22px;top:60px;width:144px;height:172px;background:linear-gradient(#6e1020,#e0123a);border:2px solid var(--gold)}
.avatar-name{left:22px;top:232px;width:144px;height:24px;background:linear-gradient(var(--gold-hi),var(--gold-mid));color:var(--ink);font-size:9px;text-align:center;line-height:24px}
.profile-btn{left:24px;top:262px;width:141px;height:26px;background:linear-gradient(#ffd36a,#e29a22);border-radius:3px;color:var(--ink);font-family:"Lora",serif;font-size:16px;display:flex;align-items:center;gap:28px;padding-left:10px}
.side-btn{left:24px;width:139px;height:24px;background:linear-gradient(#2b2b2b,#060606);border-radius:4px;font-size:12px;display:flex;align-items:center;gap:10px;padding-left:10px}
.side-btn svg{width:16px;height:16px}

/* game tabs */
.tab{top:50px;height:42px;background:linear-gradient(#ffd76f,#d8921f);border-radius:4px;font-family:"Lora",serif;font-size:20px;color:var(--white);text-shadow:0 1px 1px #7a4a0c;display:flex;align-items:center;justify-content:center}
.tab.active{background:linear-gradient(#a44a38,#5f1710);border:2px solid var(--gold)}
.tab-icon{top:42px;width:58px;height:54px;border-radius:6px}

/* dealer cards */
.dealer{background:linear-gradient(#555,#222);border-radius:8px;border:2px solid #777}
.dealer.main{background:linear-gradient(#ffd46a,#c47e16);border-color:var(--gold-dk)}
.dealer-photo{background:linear-gradient(#a02a30,#3a0c10)}
.road{background-color:#fff;background-image:conic-gradient(var(--grid) 25%,#fff 0 50%,var(--grid) 0 75%,#fff 0);background-size:28px 28px}
.road svg{width:100%;height:100%}
.dealer-bar{background:#111;border-radius:10px;display:flex;align-items:center;justify-content:space-between;padding-left:18px;font-size:13px;overflow:hidden}
.deals{background:var(--navy);height:100%;display:flex;align-items:center;padding:0 6px}

/* filter bar */
.filterbar{left:192px;top:232px;width:1008px;height:40px;background:linear-gradient(#c88420,#8b540d)}
.multi-tab{left:212px;top:238px;width:144px;height:32px;background:linear-gradient(#a44a38,#5f1710);border:1px solid var(--gold);border-radius:4px 4px 0 0;font-size:11px;display:flex;align-items:center;gap:10px;padding-left:18px}
.search{left:357px;top:238px;width:290px;height:32px;background:linear-gradient(#c98a2a,#b47414);border:1px solid #e3a544;border-radius:3px}
.fbtn{top:238px;height:32px;background:linear-gradient(#ffd46a,#e0961e);border-radius:3px;color:var(--ink);font-family:"Lora",serif;font-size:14px;display:flex;align-items:center;justify-content:center;gap:6px}

/* tables */
.lobby{left:192px;top:272px;width:1008px;height:363px;background:#0f0f0f}
.table-card{width:312px;height:157px;background:linear-gradient(#e6a233,#8b540d);border-radius:6px;padding:5px}
.table-inner{position:relative;width:100%;height:100%;background:linear-gradient(#2a8a3a,var(--felt-dk));border-radius:4px;overflow:hidden}
.table-head{position:absolute;left:0;top:0;width:100%;height:42px;background:linear-gradient(#ffd46a,#c98219);border-radius:4px}
.table-head .inner{position:absolute;left:3px;top:3px;right:3px;bottom:3px;background:linear-gradient(#1c7a2c,#0d4c1a);border-radius:3px;font-family:"Lora",serif;font-size:13px;padding:2px 6px;line-height:17px}
.commission{position:absolute;right:6px;top:2px;font-size:11px}
.seats{position:absolute;right:6px;top:20px;font-size:11px}
.join{position:absolute;left:94px;top:28px;width:122px;height:38px;background:linear-gradient(#fff3a8,#f3c43c 50%,#c58a14);border:1px solid #8a5a12;color:var(--ink);font-family:"Lora",serif;font-weight:700;font-size:14px;display:flex;align-items:center;justify-content:center}
.board{position:absolute;left:2px;top:60px;width:300px;height:60px}
.seat-row{position:absolute;left:3px;bottom:4px;display:flex;gap:3px}
.seat{width:38px;height:25px;border-radius:8px;background:#0b2a10;border:2px solid var(--gold);display:flex;align-items:center;justify-content:center}
.seat svg{width:22px;height:20px}
.seat.more{width:40px;background:linear-gradient(#ffd46a,#c98219)}

/* bottom */
.bottombar{left:0;top:637px;width:1200px;height:38px;background:linear-gradient(#2a2a2a,#050505)}
.bottom-split{left:170px;top:637px;width:4px;height:38px;background:#000}
.balance{left:931px;top:642px;width:262px;height:28px;border:1px solid #888;display:flex;font-size:14px;background:#000}
.balance .label{background:var(--navy);width:76px;display:flex;align-items:center;justify-content:center}
.balance .cur{background:linear-gradient(#ffd46a,#c98219);color:var(--ink);width:46px;display:flex;align-items:center;justify-content:center;font-size:12px;font-weight:700}
.balance .amount{flex:1;display:flex;align-items:center;justify-content:center;font-size:15px}
</style>
</head>
<body>
<svg width="0" height="0" style="position:absolute">
  <defs>
    <symbol id="person" viewBox="0 0 22 20"><circle cx="11" cy="6" r="5" fill="#fff4a0"/><path d="M2 20c0-6 4-8 9-8s9 2 9 8z" fill="#fff4a0"/></symbol>
    <symbol id="arrow" viewBox="0 0 22 20"><path d="M3 5h16l-8 11z" fill="#3a2204"/></symbol>
    <symbol id="board" viewBox="0 0 300 60">
      <g stroke="#fff" stroke-width="1.4" fill="none">
        <polygon points="30,2 270,2 292,58 8,58"/>
        <line x1="25" y1="16" x2="275" y2="16"/><line x1="17" y1="37" x2="283" y2="37"/>
        <line x1="64" y1="2" x2="49" y2="58"/><line x1="99" y1="2" x2="89" y2="58"/><line x1="133" y1="2" x2="130" y2="58"/>
        <line x1="167" y1="2" x2="170" y2="58"/><line x1="201" y1="2" x2="211" y2="58"/><line x1="236" y1="2" x2="251" y2="58"/>
      </g>
      <g fill="#fff" font-family="Lora,serif" font-style="italic" font-weight="700" font-size="12" text-anchor="middle">
        <text x="41" y="31">B</text><text x="79" y="31">B</text><text x="116" y="31">B</text><text x="150" y="31">B</text><text x="185" y="31">B</text><text x="222" y="31">B</text><text x="259" y="31">B</text>
        <text x="33" y="52">P</text><text x="71" y="52">P</text><text x="111" y="52">P</text><text x="150" y="52">P</text><text x="190" y="52">P</text><text x="230" y="52">P</text><text x="269" y="52">P</text>
      </g>
    </symbol>
    <symbol id="beads" viewBox="0 0 168 88">
      <g fill="none" stroke-width="2">
        <circle cx="7" cy="7" r="5" stroke="#c62828"/><circle cx="7" cy="21" r="5" stroke="#1e3a9e"/><circle cx="21" cy="21" r="5" stroke="#1e3a9e"/>
        <circle cx="35" cy="7" r="5" stroke="#c62828"/><circle cx="35" cy="21" r="5" stroke="#1e3a9e"/><circle cx="49" cy="7" r="5" stroke="#c62828"/>
        <circle cx="49" cy="21" r="5" stroke="#c62828"/><circle cx="63" cy="7" r="5" stroke="#c62828"/><circle cx="77" cy="7" r="5" stroke="#1e3a9e"/>
        <circle cx="91" cy="7" r="5" stroke="#c62828"/><circle cx="105" cy="7" r="5" stroke="#1e3a9e"/><circle cx="119" cy="7" r="5" stroke="#c62828"/>
        <circle cx="119" cy="21" r="5" stroke="#1e3a9e"/><circle cx="133" cy="7" r="5" stroke="#c62828"/><circle cx="133" cy="21" r="5" stroke="#c62828"/>
        <circle cx="133" cy="35" r="5" stroke="#c62828"/><circle cx="133" cy="49" r="5" stroke="#c62828"/><circle cx="133" cy="63" r="5" stroke="#c62828"/>
        <circle cx="147" cy="7" r="5" stroke="#1e3a9e"/><circle cx="147" cy="21" r="5" stroke="#1e3a9e"/>
      </g>
    </symbol>
  </defs>
</svg>

<div class="abs topbar"></div>
<div class="abs title-plate"></div>
<div class="abs title">Live Casino</div>
<div class="abs sys-icons">
  <svg viewBox="0 0 24 24"><rect x="2" y="2" width="20" height="20" rx="3" fill="#f0b23a"/><circle cx="11" cy="11" r="5" fill="none" stroke="#1b1308" stroke-width="2"/><path d="M15 15l4 4" stroke="#1b1308" stroke-width="2"/><path d="M9 11h4" stroke="#1b1308" stroke-width="2"/></svg>
  <svg viewBox="0 0 24 24"><rect x="2" y="2" width="20" height="20" rx="3" fill="#f0b23a"/><circle cx="11" cy="11" r="5" fill="none" stroke="#1b1308" stroke-width="2"/><path d="M15 15l4 4M9 11h4M11 9v4" stroke="#1b1308" stroke-width="2"/></svg>
  <svg viewBox="0 0 24 24"><path d="M8 18V5l12-2v13" stroke="#f0b23a" stroke-width="2.5" fill="none"/><circle cx="6" cy="18" r="3" fill="#f0b23a"/><circle cx="18" cy="16" r="3" fill="#f0b23a"/></svg>
  <svg viewBox="0 0 24 24"><rect x="2" y="2" width="20" height="20" fill="none" stroke="#f0b23a" stroke-width="2"/><path d="M5 5l14 14M19 5L5 19" stroke="#f0b23a" stroke-width="2"/></svg>
  <svg viewBox="0 0 24 24"><path d="M4 4l16 16M20 4L4 20" stroke="#f0b23a" stroke-width="3.5"/></svg>
</div>

<aside class="abs sidebar"></aside>
<div class="abs avatar-frame"></div>
<div class="abs avatar" role="img" aria-label="Player avatar"></div>
<div class="abs avatar-name">Name</div>
<div class="abs profile-btn"><svg width="16" height="18" viewBox="0 0 16 18"><rect x="1" y="1" width="14" height="16" fill="#6a3f08"/><path d="M4 6h8M4 9h8M4 12h8" stroke="#fde08a"/></svg>Profile</div>
<div class="abs side-btn" style="top:314px"><svg viewBox="0 0 16 16"><path d="M4 5a5 5 0 0 1 0 6M7 3a8 8 0 0 1 0 10M10 1a11 11 0 0 1 0 14" stroke="#f0b23a" fill="none" stroke-width="1.5"/></svg>Announcements</div>
<div class="abs side-btn" style="top:342px;font-size:11px"><svg viewBox="0 0 16 16"><rect x="2" y="1" width="12" height="14" fill="#f0b23a"/><path d="M8 4v5M8 11v2" stroke="#1b1308" stroke-width="2"/></svg>Rules &amp; Regulation</div>
<div class="abs side-btn" style="top:369px"><svg viewBox="0 0 16 16"><rect x="1" y="1" width="14" height="14" fill="#f0b23a"/><circle cx="7" cy="7" r="3.5" fill="none" stroke="#1b1308" stroke-width="1.5"/><path d="M10 10l3 3" stroke="#1b1308" stroke-width="1.5"/></svg>Quick Tour</div>

<div class="abs tab active" style="left:198px;width:242px;padding-left:40px">Baracat</div>
<div class="abs tab-icon" style="left:196px;background:linear-gradient(135deg,#fff,#ddd)" role="img" aria-label="Playing cards"></div>
<div class="abs tab" style="left:450px;width:222px;padding-left:36px">Super Six</div>
<div class="abs tab-icon" style="left:452px;top:46px;width:52px;height:44px;background:linear-gradient(135deg,#fff,#c33)" role="img" aria-label="Cards with number six chip"></div>
<div class="abs tab" style="left:685px;width:220px;padding-left:56px">Roulette</div>
<div class="abs tab-icon" style="left:685px;width:56px;border-radius:50%;background:radial-gradient(#caa24a,#1d6a2a 45%,#7a1a10 65%,#c98219)" role="img" aria-label="Roulette wheel"></div>
<div class="abs tab" style="left:918px;width:224px;padding-left:36px">Sic Bo</div>
<div class="abs tab-icon" style="left:916px;top:44px;width:60px;height:50px;background:linear-gradient(135deg,#e03030,#8a1010)" role="img" aria-label="Red dice"></div>

<div class="abs dealer main" style="left:206px;top:100px;width:274px;height:126px"></div>
<div class="abs dealer-photo" style="left:220px;top:107px;width:84px;height:88px" role="img" aria-label="Dealer photo"></div>
<div class="abs road" style="left:307px;top:107px;width:168px;height:88px"><svg viewBox="0 0 168 88"><use href="#beads"/></svg></div>
<div class="abs dealer-bar" style="left:215px;top:197px;width:261px;height:23px;font-size:14px">Dealer Name<span class="deals">Deals 999</span></div>

<div class="abs dealer" style="left:495px;top:96px;width:224px;height:114px"></div>
<div class="abs dealer-photo" style="left:506px;top:103px;width:68px;height:78px" role="img" aria-label="Dealer photo"></div>
<div class="abs road" style="left:577px;top:103px;width:136px;height:78px"><svg viewBox="0 0 168 88" preserveAspectRatio="xMinYMin meet"><use href="#beads"/></svg></div>
<div class="abs dealer-bar" style="left:503px;top:182px;width:209px;height:20px">Dealer Name<span class="deals">Deals 999</span></div>

<div class="abs dealer" style="left:729px;top:96px;width:226px;height:114px"></div>
<div class="abs dealer-photo" style="left:740px;top:103px;width:68px;height:78px" role="img" aria-label="Dealer photo"></div>
<div class="abs road" style="left:811px;top:103px;width:136px;height:78px"><svg viewBox="0 0 168 88" preserveAspectRatio="xMinYMin meet"><use href="#beads"/></svg></div>
<div class="abs dealer-bar" style="left:737px;top:182px;width:210px;height:20px">Dealer Name<span class="deals">Deals 999</span></div>

<div class="abs dealer" style="left:963px;top:96px;width:233px;height:114px"></div>
<div class="abs dealer-photo" style="left:975px;top:103px;width:68px;height:78px" role="img" aria-label="Dealer photo"></div>
<div class="abs road" style="left:1046px;top:103px;width:136px;height:78px"><svg viewBox="0 0 168 88" preserveAspectRatio="xMinYMin meet"><use href="#beads"/></svg></div>
<div class="abs dealer-bar" style="left:972px;top:182px;width:210px;height:20px">Dealer Name<span class="deals">Deals 999</span></div>

<div class="abs filterbar"></div>
<div class="abs multi-tab"><svg width="22" height="16" viewBox="0 0 22 16"><circle cx="7" cy="5" r="4" fill="#fde08a"/><circle cx="15" cy="5" r="4" fill="#f0b23a"/><path d="M0 16c0-5 3-6 7-6s7 1 7 6zM8 16c0-5 3-6 7-6s7 1 7 6z" fill="#fde08a"/></svg>Multiplayer</div>
<div class="abs search"></div>
<div class="abs fbtn" style="left:667px;width:104px">Join any</div>
<div class="abs fbtn" style="left:780px;width:42px;font-size:12px">A➔Z</div>
<div class="abs fbtn" style="left:826px;width:41px">$⬇</div>
<div class="abs fbtn" style="left:872px;width:43px">$⬆</div>
<div class="abs fbtn" style="left:937px;width:41px"><svg width="22" height="16" viewBox="0 0 22 16"><path d="M2 16c0-5 3-6 6-6s6 1 6 6zM8 16c0-5 3-6 6-6s6 1 6 6z" fill="#1b1308"/><circle cx="8" cy="5" r="3.5" fill="#1b1308"/><circle cx="14" cy="5" r="3.5" fill="#1b1308"/></svg></div>
<div class="abs fbtn" style="left:984px;width:41px">&lt;3</div>
<div class="abs fbtn" style="left:1030px;width:43px">&gt;3</div>
<div class="abs fbtn" style="left:1078px;width:102px">All Limits <svg width="12" height="8" viewBox="0 0 12 8"><path d="M0 0h12L6 8z" fill="#1b1308"/></svg></div>

<main class="abs lobby"></main>

<div class="abs table-card" style="left:207px;top:285px">
  <div class="table-inner">
    <div class="table-head"><div class="inner">Baccarat A5-3C<br>Bet Limit<span class="commission">Commission 0/7</span><span class="seats">0/100</span></div></div>
    <div class="join">Join</div>
    <svg class="board"><use href="#board"/></svg>
    <div class="seat-row"><div class="seat"><svg><use href="#person"/></svg></div><div class="seat"><svg><use href="#person"/></svg></div><div class="seat"><svg><use href="#person"/></svg></div><div class="seat"><svg><use href="#person"/></svg></div><div class="seat"><svg><use href="#person"/></svg></div><div class="seat more"><svg><use href="#arrow"/></svg></div><div class="seat more"><svg><use href="#arrow"/></svg></div></div>
  </div>
</div>
<div class="abs table-card" style="left:538px;top:285px">
  <div class="table-inner">
    <div class="table-head"><div class="inner">Baccarat A5-3C<br>Bet Limit<span class="commission">Commission 0/7</span><span class="seats">0/100</span></div></div>
    <div class="join">Join</div>
    <svg class="board"><use href="#board"/></svg>
    <div class="seat-row"><div class="seat"><svg><use href="#person"/></svg></div><div class="seat"><svg><use href="#person"/></svg></div><div class="seat"><svg><use href="#person"/></svg></div><div class="seat"><svg><use href="#person"/></svg></div><div class="seat"><svg><use href="#person"/></svg></div><div class="seat more"><svg><use href="#arrow"/></svg></div><div class="seat more"><svg><use href="#arrow"/></svg></div></div>
  </div>
</div>
<div class="abs table-card" style="left:870px;top:285px">
  <div class="table-inner">
    <div class="table-head"><div class="inner">Baccarat A5-3C<br>Bet Limit<span class="commission">Commission 0/7</span><span class="seats">0/100</span></div></div>
    <div class="join">Join</div>
    <svg class="board"><use href="#board"/></svg>
    <div class="seat-row"><div class="seat"><svg><use href="#person"/></svg></div><div class="seat"><svg><use href="#person"/></svg></div><div class="seat"><svg><use href="#person"/></svg></div><div class="seat"><svg><use href="#person"/></svg></div><div class="seat"><svg><use href="#person"/></svg></div><div class="seat more"><svg><use href="#arrow"/></svg></div><div class="seat more"><svg><use href="#arrow"/></svg></div></div>
  </div>
</div>
<div class="abs table-card" style="left:207px;top:456px">
  <div class="table-inner">
    <div class="table-head"><div class="inner">Baccarat A5-3C<br>Bet Limit<span class="commission">Commission 0/7</span><span class="seats">0/100</span></div></div>
    <div class="join">Join</div>
    <svg class="board"><use href="#board"/></svg>
    <div class="seat-row"><div class="seat"><svg><use href="#person"/></svg></div><div class="seat"><svg><use href="#person"/></svg></div><div class="seat"><svg><use href="#person"/></svg></div><div class="seat"><svg><use href="#person"/></svg></div><div class="seat"><svg><use href="#person"/></svg></div><div class="seat more"><svg><use href="#arrow"/></svg></div><div class="seat more"><svg><use href="#arrow"/></svg></div></div>
  </div>
</div>
<div class="abs table-card" style="left:538px;top:456px">
  <div class="table-inner">
    <div class="table-head"><div class="inner">Baccarat A5-3C<br>Bet Limit<span class="commission">Commission 0/7</span><span class="seats">0/100</span></div></div>
    <div class="join">Join</div>
    <svg class="board"><use href="#board"/></svg>
    <div class="seat-row"><div class="seat"><svg><use href="#person"/></svg></div><div class="seat"><svg><use href="#person"/></svg></div><div class="seat"><svg><use href="#person"/></svg></div><div class="seat"><svg><use href="#person"/></svg></div><div class="seat"><svg><use href="#person"/></svg></div><div class="seat more"><svg><use href="#arrow"/></svg></div><div class="seat more"><svg><use href="#arrow"/></svg></div></div>
  </div>
</div>
<div class="abs table-card" style="left:870px;top:456px">
  <div class="table-inner">
    <div class="table-head"><div class="inner">Baccarat A5-3C<br>Bet Limit<span class="commission">Commission 0/7</span><span class="seats">0/100</span></div></div>
    <div class="join">Join</div>
    <svg class="board"><use href="#board"/></svg>
    <div class="seat-row"><div class="seat"><svg><use href="#person"/></svg></div><div class="seat"><svg><use href="#person"/></svg></div><div class="seat"><svg><use href="#person"/></svg></div><div class="seat"><svg><use href="#person"/></svg></div><div class="seat"><svg><use href="#person"/></svg></div><div class="seat more"><svg><use href="#arrow"/></svg></div><div class="seat more"><svg><use href="#arrow"/></svg></div></div>
  </div>
</div>

<footer class="abs bottombar"></footer>
<div class="abs bottom-split"></div>
<div class="abs balance"><span class="label">Balance</span><span class="cur">$SGD ‹</span><span class="amount">999,999.999</span></div>
</body>
</html>
```